We need to have 2 different retractable banners designed that will be used at a variety of events. We plan to have the banners printed through printvanta.example. According to their site, specs are as follows: Retractable banners are digitally printed on 12oz double-sided smooth vinyl. While the area on the retractable banners is 33 x 78, the customer will want to provide a file that has an area of 35 x 82 to account for bleed, with 3" of that vertical bleed at the bottom of the design. Recommneded DPI is 150. Upload capacity for retractable banners is 100MP.

Banner #1: Cascade Talent Alliance logo at top; then the following text placed lower on the banner: Providing leadership that promotes and advances Oregon's workforce system. At the bottom of banner: cascadetalent alliance.example

Banner #2: Cascade Talent Alliance logo at top; then the following text placed lower on the banner: Oregon's workforce system ensures all Oregonians possess the talent needed for communities to thrive and prosper. At the bottom of banner: cascadetalentalliance.example

Color scheme: complimentary colors of the Cascade Talent Alliance logo.
Images: images representative of Oregon (for example: map of Oregon, Douglas fir trees, coastal range, etc.

I've attached a couple of previous banners created as a reference.

```html
<!DOCTYPE html>
<html lang="en">
<head>
<meta charset="utf-8">
<title>Cascade Talent Alliance – Retractable Banners</title>
<link href="https://fonts.googleapis.com/css2?family=Open+Sans:wght@400;600;700&display=swap" rel="stylesheet">
<style>
  :root {
    --navy: #263c85;
    --magenta: #a3195b;
    --maroon: #6c0f3a;
    --rose: #c9457f;
    --paper: #ffffff;
    --backdrop: #e9eaec;
    --ink: #283a7d;
  }
  html, body {
    margin: 0;
    width: 1200px;
    height: 1066px;
    overflow: hidden;
    background: var(--backdrop);
    font-family: "Open Sans", Arial, sans-serif;
  }
  .canvas {
    position: relative;
    width: 1200px;
    height: 1066px;
  }
  .banner {
    position: absolute;
    top: 125px;
    width: 356px;
    height: 815px;
    background: var(--paper);
    overflow: hidden;
  }
  .banner--leadership { left: 185px; }
  .banner--talent { left: 665px; }
  .banner__layer {
    position: absolute;
    inset: 0;
    width: 356px;
    height: 815px;
  }
  .banner__brand {
    position: absolute;
    top: 38px;
    left: 0;
    right: 0;
    text-align: center;
    color: var(--navy);
    font-weight: 600;
    font-size: 15px;
    letter-spacing: 0.12em;
    text-transform: uppercase;
    line-height: 1.3;
  }
  .banner__brand-mark {
    display: block;
    width: 44px;
    height: 44px;
    margin: 0 auto 12px;
    background: var(--magenta);
  }
  .banner__message {
    position: absolute;
    margin: 0;
    color: var(--ink);
    font-weight: 400;
    font-size: 20px;
    line-height: 1.36;
  }
  .banner--leadership .banner__message {
    top: 540px;
    right: 34px;
    width: 180px;
    text-align: right;
  }
  .banner--talent .banner__message {
    top: 512px;
    left: 38px;
    width: 190px;
    text-align: left;
  }
  .banner__url {
    position: absolute;
    bottom: 26px;
    left: 0;
    right: 0;
    text-align: center;
    margin: 0;
    color: var(--navy);
    font-weight: 700;
    font-size: 14px;
  }
</style>
</head>
<body>
<main class="canvas">

  <section class="banner banner--leadership">
    <svg class="banner__layer" viewBox="0 0 356 815" aria-hidden="true">
      <path d="M0 0H78C56 150 22 270 66 430C104 570 30 690 70 815H0Z" fill="var(--rose)" opacity="0.55"/>
      <path d="M0 0H56C76 140 80 260 44 410C12 545 84 660 58 815H0Z" fill="var(--magenta)" opacity="0.8"/>
      <path d="M0 0H46C52 160 24 300 58 455C84 590 34 700 48 815H0Z" fill="var(--maroon)" opacity="0.65"/>
      <rect x="0" y="0" width="38" height="815" fill="var(--navy)"/>
    </svg>
    <svg class="banner__layer" viewBox="0 0 356 815" role="img" aria-label="Photograph of a snow-capped volcanic peak above an evergreen forest reflected in a calm lake">
      <defs>
        <linearGradient id="mountain-scene" x1="0" y1="0" x2="0" y2="1">
          <stop offset="0" stop-color="#7fa3cf"/>
          <stop offset="0.35" stop-color="#dfe6ee"/>
          <stop offset="0.55" stop-color="#3f6b3a"/>
          <stop offset="0.8" stop-color="#1f3a2a"/>
          <stop offset="1" stop-color="#6d8fb0"/>
        </linearGradient>
      </defs>
      <path d="M38 235C140 172 262 168 356 196V425C300 398 250 400 200 425C140 455 90 475 38 458Z" fill="url(#mountain-scene)"/>
    </svg>
    <div class="banner__brand">
      <span class="banner__brand-mark"></span>
      Cascade Talent<br>Alliance
    </div>
    <p class="banner__message">Providing leadership that promotes and advances Oregon's workforce system</p>
    <p class="banner__url">cascadetalent alliance.example</p>
  </section>

  <section class="banner banner--talent">
    <svg class="banner__layer" viewBox="0 0 356 815" aria-hidden="true">
      <g transform="translate(356 0) scale(-1 1)">
        <path d="M0 0H78C56 150 22 270 66 430C104 570 30 690 70 815H0Z" fill="var(--rose)" opacity="0.55"/>
        <path d="M0 0H56C76 140 80 260 44 410C12 545 84 660 58 815H0Z" fill="var(--magenta)" opacity="0.8"/>
        <path d="M0 0H46C52 160 24 300 58 455C84 590 34 700 48 815H0Z" fill="var(--maroon)" opacity="0.65"/>
        <rect x="0" y="0" width="38" height="815" fill="var(--navy)"/>
      </g>
    </svg>
    <svg class="banner__layer" viewBox="0 0 356 815" role="img" aria-label="Photograph of a white coastal lighthouse on a grassy headland under a cloudy sky">
      <defs>
        <linearGradient id="coast-scene" x1="0" y1="0" x2="0" y2="1">
          <stop offset="0" stop-color="#7e93ad"/>
          <stop offset="0.45" stop-color="#c9d2dc"/>
          <stop offset="0.75" stop-color="#b9bcc0"/>
          <stop offset="1" stop-color="#5f7040"/>
        </linearGradient>
      </defs>
      <path d="M0 205C90 170 220 168 318 230V450C266 470 210 452 150 425C100 400 50 398 0 420Z" fill="url(#coast-scene)"/>
    </svg>
    <div class="banner__brand">
      <span class="banner__brand-mark"></span>
      Cascade Talent<br>Alliance
    </div>
    <p class="banner__message">Oregon's workforce system ensures all Oregonians possess the talent needed for communities to thrive and prosper</p>
    <p class="banner__url">cascadetalent alliance.example</p>
  </section>

</main>
</body>
</html>
```